Business Card Design

We would like to re-design our business cards. Our Company - Qoralin Turbochargers, rebuilds turbochargers and sells replacement parts. Our website is: http://www.qoralinturbochargers-example.com
We just had our logo changed. I will attach the file. Looking for fresh new/modern business card. We like the colors red, black, white and silver. Black background looks attractive, but not a requirement. The final design should communicate reasonable/competitive prices, top quality and reliability of our products.
Updates
Project Deadline Extended
Reason: Need to finalize the info on the card. Currently working on changing address and email info. Want to make sure it is the correct one before accepting the final design. Unless, this is something that can be changed at a later time..??
Industry/Entity Type
Business
Contact Information for Business Card
QORALIN TURBOCHARGERS, LLC
20473 Pemberly Road NE
Massillon, OH 44012
Tel: +1-330-555-0162
Fax: +1-330-555-0187
info@QoralinTurbochargers-example.com
Our current business card had the following highlights:
*We rebuild all Turbocharges for Automotive, Diesel and Industrial
*Precision Balancing and in-house turbocharger needs
*All Turbocharger replacement parts are made in USA / U.K.
Look and feel
Each slider illustrates characteristics of the customer's brand and the style your logo design should communicate.

```html
<!DOCTYPE html>
<html lang="en">
<head>
<meta charset="utf-8">
<title>Qoralin Turbochargers – Business Card</title>
<link rel="stylesheet" href="https://fonts.googleapis.com/css2?family=Open+Sans:wght@400;700&display=swap">
<style>
  :root {
    --bg: #2a2a2c;
    --card-white: #f4f4f4;
    --brand-red: #d42a2f;
    --brand-red-dark: #c22428;
    --ink: #1e1e1e;
    --ink-soft: #333333;
  }
  * { box-sizing: border-box; margin: 0; padding: 0; }
  html, body { width: 1200px; height: 800px; overflow: hidden; }
  body {
    background: var(--bg);
    font-family: "Open Sans", sans-serif;
    position: relative;
  }
  .card {
    position: absolute;
    top: 250px;
    width: 525px;
    height: 300px;
    border-radius: 4px;
    overflow: hidden;
  }
  .card--front { left: 55px; background: var(--card-white); }
  .card--back { left: 620px; background: var(--brand-red); }

  .brand {
    position: absolute;
    display: flex;
    align-items: center;
    gap: 10px;
    font-weight: 700;
    white-space: nowrap;
  }
  .brand__dot { width: 14px; height: 14px; border-radius: 50%; }
  .card--front .brand { top: 40px; left: 190px; font-size: 26px; color: var(--ink); }
  .card--front .brand__dot { background: var(--brand-red); }
  .card--back .brand { top: 126px; left: 60px; font-size: 34px; color: var(--ink); }
  .card--back .brand__dot { background: var(--ink); width: 18px; height: 18px; }

  .person { position: absolute; top: 98px; left: 36px; }
  .person__name { font-size: 22px; color: var(--brand-red); font-weight: 400; line-height: 1.1; }
  .person__title { font-size: 12px; color: var(--ink); }

  .contacts {
    position: absolute; top: 150px; left: 36px;
    list-style: none; font-size: 13px; color: var(--ink-soft);
  }
  .contacts li { display: flex; align-items: center; gap: 8px; height: 19px; white-space: nowrap; }
  .contacts svg { width: 12px; height: 12px; fill: var(--brand-red); flex: none; }

  .address {
    position: absolute; top: 228px; right: 30px;
    text-align: right; font-size: 15px; line-height: 1.3;
    font-style: normal; color: var(--ink);
  }

  .stripes { position: absolute; left: 0; right: 0; bottom: 0; }
  .stripe { display: block; width: 100%; }
  .stripe--red { height: 12px; background: var(--brand-red); }
  .stripe--black { height: 7px; background: var(--ink); }
  .stripe--edge { height: 10px; background: var(--brand-red-dark); }
</style>
</head>
<body>
  <section class="card card--front" aria-label="Business card front">
    <div class="brand"><span class="brand__dot"></span>Qoralin Turbochargers</div>

    <div class="person">
      <p class="person__name">Marten Hollis</p>
      <p class="person__title">Director</p>
    </div>

    <ul class="contacts">
      <li>
        <svg viewBox="0 0 12 12" aria-hidden="true"><path d="M2.5 0.5l2 2-1 1.5c.7 1.5 1.8 2.6 3.3 3.3L8.3 6.3l2 2-1.3 1.9C5 10 1.8 6.8 0.8 2z"/></svg>
        +1-330-555-0162
      </li>
      <li>
        <svg viewBox="0 0 12 12" aria-hidden="true"><path d="M3 0h6v3H3zM1 4h10v5H9v3H3V9H1zM4 8v3h4V8z"/></svg>
        +1-330-555-0187
      </li>
      <li>
        <svg viewBox="0 0 12 12" aria-hidden="true"><path d="M0 2h12v8H0zM1 3l5 4 5-4v-.2H1z" fill-rule="evenodd"/></svg>
        info@QoralinTurbochargers-example.com
      </li>
      <li>
        <svg viewBox="0 0 12 12" aria-hidden="true"><path d="M6 0a6 6 0 1 0 0 12A6 6 0 0 0 6 0zm0 1c.8 0 1.6 1.9 1.8 4H4.2C4.4 2.9 5.2 1 6 1zM1.05 5h2.15a10 10 0 0 1 .9-3.6A5 5 0 0 0 1.05 5zm7.75 0h2.15a5 5 0 0 0-3.05-3.6A10 10 0 0 1 8.8 5zM1.05 7a5 5 0 0 0 3.05 3.6A10 10 0 0 1 3.2 7zm3.15 0c.2 2.1 1 4 1.8 4s1.6-1.9 1.8-4zm4.6 0a10 10 0 0 1-.9 3.6A5 5 0 0 0 10.95 7z"/></svg>
        www.qoralinturbochargers-example.com
      </li>
    </ul>

    <address class="address">
      5218 Ashgrove Ave. NW<br>
      North Calderwood.Ohio
    </address>

    <div class="stripes" aria-hidden="true">
      <span class="stripe stripe--red"></span>
      <span class="stripe stripe--black"></span>
      <span class="stripe stripe--edge"></span>
    </div>
  </section>

  <section class="card card--back" aria-label="Business card back">
    <div class="brand"><span class="brand__dot"></span>Qoralin Turbochargers</div>
  </section>
</body>
</html>
```